Criação de Power Point Slide Mestre para Automotivo
A empresa queria:
" Tavo Nexa é uma empresa que prove facil e rapido acesso para estacionamentos em shopping centers, condominio , aeroportos. Nos fazemos isto primariamente usando tecnologia RFID ( tantos tags quanto leitores ) mas nao esta limitada apenas a esta tecnologia e pode migrar para telefone via QRCODE e tambem cameras OCR para capturar a placa dos carros no futuro "

```html
<!DOCTYPE html>
<html lang="pt-BR">
<head>
<meta charset="UTF-8">
<title>Tavo Nexa — Slide Mestre</title>
<link rel="stylesheet" href="https://fonts.googleapis.com/css2?family=Montserrat:wght@600;700&family=Open+Sans:wght@400&display=swap">
<style>
  :root {
    --page-bg: #e9e9ea;
    --slide-light: #f4f4f5;
    --slide-mid: #dcdde0;
    --title-ink: #3a3b3f;
    --body-ink: #55575c;
    --gold: #b8894a;
    --gold-light: #d9b27a;
    --brand-ink: #2f3e63;
    --photo-dark: #4c5250;
    --photo-green: #7d8f5a;
    --photo-gray: #9a9d9f;
  }
  * { margin: 0; padding: 0; box-sizing: border-box; }
  html, body {
    width: 1200px; height: 1200px; overflow: hidden;
    background: var(--page-bg);
  }
  .slide {
    position: absolute; left: 0; top: 262px;
    width: 1200px; height: 675px; overflow: hidden;
    background:
      linear-gradient(180deg, rgba(255,255,255,0.92) 0%, rgba(255,255,255,0.55) 20%, rgba(255,255,255,0.35) 100%),
      radial-gradient(ellipse at 25% 60%, var(--slide-light) 0%, var(--slide-mid) 70%);
  }
  .slide-title {
    position: absolute; left: 55px; top: 62px;
    display: flex; align-items: center; gap: 20px;
    font-family: "Montserrat", sans-serif; font-weight: 700;
    font-size: 40px; letter-spacing: 0.5px; color: var(--title-ink);
  }
  .title-marker { width: 46px; height: 50px; }
  .body-copy {
    position: absolute; left: 124px; top: 188px; width: 505px;
    font-family: "Open Sans", sans-serif; font-size: 20px; line-height: 29px;
    color: var(--body-ink);
  }
  .body-copy p + p { margin-top: 22px; }
  .hero-photo {
    position: absolute; left: 645px; top: 142px; width: 555px; height: 388px;
    border-radius: 30px 0 0 30px;
    background:
      linear-gradient(180deg, var(--photo-green) 0%, var(--photo-green) 8%, var(--photo-dark) 14%, var(--photo-gray) 55%, var(--photo-dark) 80%, var(--photo-green) 100%);
  }
  .footer-rule {
    position: absolute; left: 0; top: 626px; width: 930px; height: 4px;
    background: linear-gradient(90deg, var(--gold) 0%, var(--gold-light) 100%);
  }
  .brand-name {
    position: absolute; right: 40px; top: 580px;
    display: flex; align-items: center; gap: 12px;
    font-family: "Montserrat", sans-serif; font-weight: 600;
    font-size: 40px; color: var(--brand-ink);
  }
  .brand-dot { width: 14px; height: 14px; border-radius: 50%; background: var(--gold); }
</style>
</head>
<body>
  <main class="slide">
    <h1 class="slide-title">
      <svg class="title-marker" viewBox="0 0 46 50" aria-hidden="true">
        <polygon points="0,0 46,25 0,50" fill="var(--gold)"/>
        <polygon points="0,0 46,25 10,25" fill="var(--gold-light)"/>
      </svg>
      TÍTULO APRESENTAÇÃO
    </h1>

    <div class="body-copy">
      <p>Lorem ipsum dolor sit amet, consectetur nibh venenatis in ante. Etiam dui tincidunt ultricies adipiscing elit. Etiam ultrices dui sed pretium iaculis. Aliquam efficitur dui odio, eu congue augue auctor et. Donec a massa quis nisl ante sollicitudin congue at sit amet augue.</p>
      <p>Donec ac felis gravida nibh is dictum viverra Wonec diam velit, sollicitudin nec ultricies eu venenatis in ante. Etiam dui tincidunt ultricies adipiscing elit. Etiam ultrices dui sed pretium eros, fringilla pharetra purus sagittis id.</p>
    </div>

    <div class="hero-photo" role="img" aria-label="Vista aérea de carros estacionados em vagas de um estacionamento"></div>

    <div class="footer-rule"></div>

    <div class="brand-name"><span class="brand-dot"></span>Tavo Nexa</div>
  </main>
</body>
</html>
```